UNIQUE, Elegant business card for transport company.

MUST BE AN ACTUAL GRAPHIC DESIGNER.
NO TEMPLATES, NO MOCKUP GENERATORS.
Looking for a top notch, head turning, business card.
Will be printed on premium luxury paper with spot glossing and debossing.
Must know how to set up for spot glossing. Must be willing to work on the file to meet printers spec after final design.

Target Market(s)

All info on .psd file

Contact Information for Business Card

All info on .psd file

Requirements
Must have
• All info on .psd file
Nice to have
• All info on .psd file
Should not have
• Nothing red

```html
<!DOCTYPE html>
<html lang="en">
<head>
<meta charset="UTF-8">
<title>Norvane Transport business card</title>
<link rel="stylesheet" href="https://fonts.googleapis.com/css2?family=Poppins:wght@300;400;600&display=swap">
<style>
  :root {
    --page: #d9d9db;
    --card: #1c1c1e;
    --card-edge: #141415;
    --accent: #1a8fd6;
    --text-muted: #8e8e93;
    --text-soft: #a9a9ae;
    --deboss: #2e2e31;
    --deboss-text: #4a4a4e;
  }
  * { box-sizing: border-box; margin: 0; padding: 0; }
  html, body { width: 1200px; height: 800px; overflow: hidden; }
  body {
    background: var(--page);
    font-family: "Poppins", sans-serif;
    display: flex;
    align-items: center;
    justify-content: center;
    gap: 40px;
  }
  .card {
    position: relative;
    width: 540px;
    height: 308px;
    border-radius: 22px;
    background: var(--card);
    border: 1px solid var(--card-edge);
    overflow: hidden;
  }

  /* Front side */
  .brand {
    position: absolute;
    left: 0;
    top: 0;
    width: 290px;
    height: 100%;
    display: flex;
    flex-direction: column;
    align-items: center;
    justify-content: center;
    gap: 16px;
  }
  .brand-dot {
    width: 64px;
    height: 64px;
    border-radius: 50%;
    background: var(--accent);
  }
  .brand-name {
    font-size: 15px;
    font-weight: 400;
    letter-spacing: 0.12em;
    color: var(--text-muted);
    text-transform: uppercase;
  }
  .divider {
    position: absolute;
    left: 290px;
    top: 40px;
    width: 1px;
    height: 228px;
    background: var(--accent);
  }
  .details {
    position: absolute;
    left: 312px;
    top: 34px;
    right: 16px;
    color: var(--text-muted);
    font-size: 10.5px;
    font-weight: 300;
    line-height: 1.5;
  }
  .person-name {
    font-size: 22px;
    font-weight: 600;
    color: var(--accent);
    line-height: 1.1;
  }
  .person-title {
    font-size: 11px;
    color: var(--text-soft);
    margin-bottom: 6px;
  }
  .address { margin-bottom: 6px; }
  .contact-list { list-style: none; }
  .contact-list li {
    display: flex;
    align-items: center;
    gap: 8px;
  }
  .contact-list svg {
    width: 10px;
    height: 10px;
    flex: none;
    fill: none;
    stroke: var(--accent);
    stroke-width: 2;
  }

  /* Back side */
  .emblem {
    position: absolute;
    left: 50%;
    top: 44px;
    transform: translateX(-50%);
    display: flex;
    flex-direction: column;
    align-items: center;
    gap: 14px;
  }
  .emblem-dot {
    width: 110px;
    height: 110px;
    border-radius: 50%;
    background: var(--deboss);
  }
  .emblem-name {
    font-size: 16px;
    font-weight: 400;
    letter-spacing: 0.14em;
    color: var(--deboss-text);
    text-transform: uppercase;
  }
  .tagline {
    position: absolute;
    left: 0;
    right: 0;
    bottom: 34px;
    text-align: center;
    font-size: 15px;
    font-weight: 400;
    color: var(--accent);
  }
</style>
</head>
<body>

  <section class="card card-front" aria-label="Card front">
    <div class="brand">
      <span class="brand-dot"></span>
      <span class="brand-name">Norvane Transport, Inc.</span>
    </div>
    <div class="divider"></div>
    <div class="details">
      <p class="person-name">Dana Whitfield</p>
      <p class="person-title">Transporter</p>
      <p class="address">420 Alder Ridge Way, SE<br>Fairbrook, Georgia, 30412<br>US DOT 5817204<br>MC # 7702413</p>
      <ul class="contact-list">
        <li><svg viewBox="0 0 12 12"><path d="M2 1.5l2 0 1 2.5-1.3 1a6 6 0 0 0 3.3 3.3l1-1.3 2.5 1v2A1 1 0 0 1 9.5 11 8.5 8.5 0 0 1 1 2.5a1 1 0 0 1 1-1z"/></svg>(877) BOOK NRV</li>
        <li><svg viewBox="0 0 12 12"><path d="M2 1.5l2 0 1 2.5-1.3 1a6 6 0 0 0 3.3 3.3l1-1.3 2.5 1v2A1 1 0 0 1 9.5 11 8.5 8.5 0 0 1 1 2.5a1 1 0 0 1 1-1z"/></svg>(404) 555-0182</li>
        <li><svg viewBox="0 0 12 12"><rect x="3" y="1" width="6" height="10" rx="1"/></svg>(770) 555-0147</li>
        <li><svg viewBox="0 0 12 12"><rect x="3" y="1" width="6" height="10" rx="1"/></svg>(877) 555-0126</li>
        <li><svg viewBox="0 0 12 12"><rect x="1" y="2.5" width="10" height="7" rx="1"/><path d="M1 3l5 4 5-4"/></svg>dana@norvanetransport.com</li>
        <li><svg viewBox="0 0 12 12"><circle cx="6" cy="6" r="5"/><path d="M1 6h10M6 1c2.5 3 2.5 7 0 10M6 1c-2.5 3-2.5 7 0 10"/></svg>www.norvanetransport.com</li>
      </ul>
    </div>
  </section>

  <section class="card card-back" aria-label="Card back">
    <div class="emblem">
      <span class="emblem-dot"></span>
      <span class="emblem-name">Norvane Transport</span>
    </div>
    <p class="tagline">Licensed. Bonded. Insured.</p>
  </section>

</body>
</html>
```